Business Card Design Project

Company name will be Tolvan Crest (named after my black lab and his fraying muzzle) Business is in the body armor, Security product industry servicing the state, local, and federal law enforcement markets. I want a more formal and serious logo for both business cards and letterhead

```html
<!DOCTYPE html>
<html lang="en">
<head>
<meta charset="utf-8">
<title>Tolvan Crest – Business Card</title>
<link rel="stylesheet" href="https://fonts.googleapis.com/css2?family=Open+Sans:wght@300;400;700;800&display=swap">
<style>
  :root {
    --card-bg: #3a3a3a;
    --card-sheen: #cfcfcf;
    --ink-light: #ffffff;
    --ink-soft: #f2f2f2;
    --mark-fill: #b9b9b9;
    --rule: #ffffff;
  }
  * { margin: 0; padding: 0; box-sizing: border-box; }
  html, body {
    width: 777px;
    height: 1200px;
    overflow: hidden;
    background: var(--card-bg);
  }
  .card {
    position: relative;
    width: 777px;
    height: 1200px;
    background:
      linear-gradient(135deg, var(--card-sheen) 0%, #8a8a8a 12%, #4a4a4a 30%, var(--card-bg) 45%, var(--card-bg) 100%);
    font-family: "Open Sans", Arial, sans-serif;
    color: var(--ink-light);
    text-align: center;
  }
  .brand-square {
    position: absolute;
    left: 288px;
    top: 100px;
    width: 200px;
    height: 200px;
    background: var(--mark-fill);
  }
  .brand-name {
    position: absolute;
    left: 0;
    right: 0;
    top: 400px;
    font-weight: 800;
    font-size: 132px;
    line-height: 140px;
    letter-spacing: -2px;
    color: var(--ink-light);
  }
  .brand-tagline {
    position: absolute;
    left: 0;
    right: 0;
    top: 714px;
    font-weight: 700;
    font-size: 17px;
    letter-spacing: 10px;
    color: var(--ink-light);
  }
  .brand-tagline .divider {
    display: inline-block;
    width: 3px;
    height: 16px;
    background: var(--rule);
    margin: 0 34px 0 24px;
    vertical-align: -2px;
  }
  .contact-name {
    position: absolute;
    left: 0; right: 0;
    top: 866px;
    font-weight: 700;
    font-size: 37px;
    letter-spacing: -0.5px;
  }
  .contact-title {
    position: absolute;
    left: 0; right: 0;
    top: 912px;
    font-weight: 300;
    font-size: 28px;
    color: var(--ink-soft);
  }
  .contact-address {
    position: absolute;
    left: 0; right: 0;
    top: 984px;
    font-weight: 300;
    font-size: 30px;
    line-height: 42px;
    color: var(--ink-soft);
  }
  .contact-lines {
    position: absolute;
    left: 0; right: 0;
    top: 1085px;
    font-weight: 700;
    font-size: 30px;
    letter-spacing: -0.3px;
  }
  .contact-lines .divider {
    display: inline-block;
    width: 3px;
    height: 36px;
    background: var(--rule);
    margin: 0 14px;
    vertical-align: -4px;
  }
</style>
</head>
<body>
  <main class="card">
    <div class="brand-square" aria-hidden="true"></div>
    <h1 class="brand-name">Tolvan<br>Crest</h1>
    <p class="brand-tagline">security<span class="divider"></span>body armor</p>

    <h2 class="contact-name">Rowan Pierce</h2>
    <p class="contact-title">Manufacturers Rep. Principal</p>
    <p class="contact-address">1740 Harbor Lane North<br>SEAGROVE BAY, FL 32099</p>
    <p class="contact-lines">f. 555-014-2287<span class="divider"></span>rpiercetc1@mailbox.com</p>
  </main>
</body>
</html>
```